Computer Security Training Brochure Needs Graphic Help!

We need a graphical artist help on our brochure. The content is there and the framework is good it's just boring and unappealing to the eye. We especially need help with the front cover. TVLK is a computer security training company that specializes in intermediate to advanced Cyber Security courses. The original design was done in Adobe In-Design and the files are included. We need something that looks very clean and professional but also is unique and cutting edge just like our customers. No generic Computer with Locks and Chains type stuff please. We want really unique and clever designs!
Updates

Project Deadline Extended
Reason: We've had request to extend the deadline on this so we're going to give another 5 days for extra time. Thanks for your designs!
Added Monday, November 17, 2014

The biggest problem we have with the original brochure is the front cover. The red triangles is basic and not appealing. Some of the newer designs submitted look way better but please don't feel like you have to use our original designs on this project we're looking for something re-worked and fresh. Thanks for your designs!

Industry/Entity Type

Computer

```html
<!DOCTYPE html>
<html lang="en">
<head>
<meta charset="UTF-8">
<title>TVLK Training Catalog 2014 - 2015</title>
<link rel="stylesheet" href="https://fonts.googleapis.com/css2?family=Roboto:wght@300&display=swap">
<style>
  :root {
    --crimson-bright: #d8212a;
    --crimson: #8e1a1f;
    --maroon: #4a0f16;
    --night: #14090d;
    --slate: #3a3b3e;
    --steel: #6e6a6c;
    --teal: #1f6f86;
    --paper: #ffffff;
  }
  html, body {
    margin: 0;
    padding: 0;
    width: 927px;
    height: 1200px;
    overflow: hidden;
    background: var(--night);
  }
  .cover {
    position: relative;
    width: 927px;
    height: 1200px;
    overflow: hidden;
    font-family: "Roboto", "Helvetica Neue", Arial, sans-serif;
    color: var(--paper);
  }
  .cover__backdrop {
    position: absolute;
    inset: 0;
    background:
      radial-gradient(ellipse 60% 40% at 30% 12%, var(--crimson-bright) 0%, rgba(216,33,42,0) 70%),
      radial-gradient(ellipse 45% 25% at 80% 98%, var(--teal) 0%, rgba(31,111,134,0) 75%),
      radial-gradient(ellipse 50% 22% at 35% 95%, var(--steel) 0%, rgba(110,106,108,0) 75%),
      linear-gradient(170deg, var(--crimson) 0%, var(--maroon) 40%, var(--night) 68%, var(--slate) 100%);
  }
  .brand {
    position: absolute;
    left: 0;
    right: 0;
    top: 600px;
    display: flex;
    align-items: center;
    justify-content: center;
    gap: 22px;
  }
  .brand__mark {
    width: 26px;
    height: 26px;
    background: var(--paper);
  }
  .brand__name {
    font-weight: 300;
    font-size: 112px;
    line-height: 1;
    letter-spacing: 4px;
    margin: 0;
  }
  .cover__years {
    position: absolute;
    left: 0;
    right: 0;
    top: 962px;
    margin: 0;
    text-align: center;
    font-weight: 300;
    font-size: 50px;
    line-height: 1;
    letter-spacing: 1px;
  }
</style>
</head>
<body>
  <main class="cover">
    <div class="cover__backdrop" role="img" aria-label="Faceted mosaic of red, charcoal and teal triangles across the cover"></div>
    <div class="brand">
      <span class="brand__mark" aria-hidden="true"></span>
      <h1 class="brand__name">TVLK</h1>
    </div>
    <p class="cover__years">2014 - 2015</p>
  </main>
</body>
</html>
```